RTV Engineering Business Card Design

We’re looking for an elegant, clean, and timeless business card design that communicates experience, capability, and reliability.

RTV Engineering was established in 1995 , we are a Government Contracting company providing Professional Services to the Department of Harbor Affairs, Frontier Resilience and the Signals Consortium. Our capabilities include: Acquisition & Program Management; Intelligence & Security Operations; Cyber, IT & Network Operations; Lifecycle Logistics & Asset Readiness; C5ISR Systems Engineering & Sustainment.

We want the card to reflect a straightforward, confident approach to business. The design should feel polished and professional without being flashy or overly corporate.

Design Direction
Clean, sophisticated, and uncluttered
Elegant but understated
Strong typography and thoughtful spacing
A timeless aesthetic rather than something overly trendy
Confident and established, with a sense of substance
Easy to read and practical in a real-world business setting

The overall impression should be: “These are experienced professionals who know what they’re doing, do what they say, and can be relied upon.”

We’re open to creative interpretations. The finished card should feel distinctive through its typography, proportions, layout, and attention to detail rather than through excessive graphics or visual effects.

We’re looking for a design that would make a potential client immediately feel that they’re dealing with a capable, trustworthy, and established company.

Company Colors: Navy and Gold/Yellow (but you do not need to use these colors on the card)
Company Name: RTV Engineering Associates, Inc. (known as RTV Engineering)
Website: rtvengineering-hq.example
Company Logo: Navy & Gold (other variations attached)

```html
<!DOCTYPE html>
<html lang="en">
<head>
<meta charset="utf-8">
<title>RTV Engineering – Business Card</title>
<link rel="stylesheet" href="https://fonts.googleapis.com/css2?family=Poppins:wght@400;500;700;800&family=Great+Vibes&display=swap">
<style>
  :root {
    --navy: #1b2453;
    --gold: #f6e64a;
    --white: #ffffff;
    --backdrop: #d9d9d9;
  }
  * { margin: 0; padding: 0; box-sizing: border-box; }
  html, body { width: 1200px; height: 2185px; overflow: hidden; }
  body { background: var(--backdrop); font-family: "Poppins", sans-serif; position: relative; }

  .card { position: absolute; left: 98px; width: 1005px; height: 575px; background: var(--white); overflow: hidden; }
  .card--front { top: 480px; }
  .card--back { top: 1120px; }
  .card__art { position: absolute; inset: 0; }

  .brand-name { position: absolute; font-weight: 800; white-space: nowrap; }
  .front__name { left: 0; width: 860px; top: 190px; text-align: center; color: var(--white); font-size: 68px; letter-spacing: 1px; }
  .front__est { position: absolute; left: 0; width: 860px; top: 318px; text-align: center; color: var(--gold); font-size: 24px; font-weight: 500; letter-spacing: 6px; }

  .back__years { position: absolute; left: 78px; top: 82px; color: var(--gold); font-family: "Great Vibes", cursive; font-size: 82px; line-height: 1; }
  .back__tagline { position: absolute; left: 70px; top: 186px; width: 292px; color: var(--white); font-size: 21px; font-weight: 500; line-height: 24px; padding-bottom: 10px; border-bottom: 1.5px solid var(--gold); }

  .contact-rail { position: absolute; left: 64px; top: 308px; width: 58px; height: 267px; background: var(--gold); border-radius: 29px 29px 0 0; }
  .contact-rail__cut { position: absolute; left: 0; width: 58px; height: 4px; background: var(--navy); }
  .contact-rail__icon { position: absolute; left: 16px; width: 26px; height: 26px; }

  .contact-list { position: absolute; left: 146px; top: 330px; width: 320px; color: var(--white); font-size: 22px; line-height: 28px; }
  .contact-item { border-bottom: 1.5px dashed rgba(255,255,255,0.35); height: 68px; display: flex; align-items: center; }
  .contact-item:last-child { border-bottom: none; align-items: flex-start; padding-top: 12px; width: 360px; }

  .services { position: absolute; left: 586px; top: 44px; width: 370px; list-style: none; }
  .service { display: flex; align-items: center; height: 73px; }
  .service__icon { width: 48px; height: 48px; border-radius: 50%; background: var(--navy); flex: none; display: flex; align-items: center; justify-content: center; }
  .service__icon span { width: 20px; height: 20px; border: 3px solid var(--gold); border-radius: 50%; }
  .service__text { margin-left: 18px; color: var(--navy); font-size: 19.5px; font-weight: 500; line-height: 24px; padding: 4px 0; flex: 1; border-bottom: 1.5px solid var(--gold); }
  .service:last-child .service__text { border-bottom: none; }

  .back__name { right: 50px; top: 486px; color: var(--navy); font-size: 28px; line-height: 40px; }
</style>
</head>
<body>

<section class="card card--front" aria-label="Card front">
  <svg class="card__art" viewBox="0 0 1005 575" aria-hidden="true">
    <path fill="var(--gold)" d="M820,4 C960,100 1020,220 985,330 C940,470 760,545 560,540 C360,535 170,460 0,395 L0,360 L820,0 Z"/>
    <path fill="var(--navy)" stroke="var(--white)" stroke-width="7" d="M0,-5 H808 C900,85 935,180 915,260 C885,380 720,470 510,468 C320,466 150,430 0,385 Z"/>
  </svg>
  <div class="brand-name front__name">RTV ENGINEERING</div>
  <div class="front__est">ESTABLISHED 1995</div>
</section>

<section class="card card--back" aria-label="Card back">
  <svg class="card__art" viewBox="0 0 1005 575" aria-hidden="true">
    <rect width="1005" height="575" fill="var(--navy)"/>
    <path fill="var(--gold)" d="M430,0 H1005 V575 H690 C560,470 410,320 420,140 C422,80 425,40 430,0 Z"/>
    <path fill="var(--white)" stroke="var(--white)" stroke-width="2" d="M505,0 H1005 V575 H700 C560,440 470,300 480,150 C484,90 492,40 505,0 Z"/>
    <path fill="none" stroke="var(--white)" stroke-width="4" d="M426,0 C410,120 405,260 500,400 C560,480 620,530 690,575"/>
  </svg>

  <div class="back__years">30 Years</div>
  <div class="back__tagline">CLEARED EXPERTISE WITH MEASURABLE IMPACT</div>

  <div class="contact-rail">
    <div class="contact-rail__cut" style="top:80px"></div>
    <div class="contact-rail__cut" style="top:146px"></div>
    <svg class="contact-rail__icon" style="top:30px" viewBox="0 0 24 24" aria-label="Phone"><path fill="var(--navy)" d="M6.6 10.8a15.1 15.1 0 0 0 6.6 6.6l2.2-2.2c.3-.3.7-.4 1-.2 1.1.4 2.3.6 3.6.6.6 0 1 .4 1 1V20c0 .6-.4 1-1 1A17 17 0 0 1 3 4c0-.6.4-1 1-1h3.5c.6 0 1 .4 1 1 0 1.3.2 2.5.6 3.6.1.3 0 .7-.2 1z"/></svg>
    <svg class="contact-rail__icon" style="top:100px" viewBox="0 0 24 24" aria-label="Website"><g fill="none" stroke="var(--navy)" stroke-width="2"><circle cx="12" cy="12" r="9"/><ellipse cx="12" cy="12" rx="4" ry="9"/><path d="M3 12h18M5 7h14M5 17h14"/></g></svg>
    <svg class="contact-rail__icon" style="top:170px" viewBox="0 0 24 24" aria-label="Address"><path fill="var(--navy)" d="M12 2a7 7 0 0 0-7 7c0 5.2 7 13 7 13s7-7.8 7-13a7 7 0 0 0-7-7zm0 9.5A2.5 2.5 0 1 1 12 6.5a2.5 2.5 0 0 1 0 5z"/></svg>
  </div>

  <div class="contact-list">
    <div class="contact-item">555 010 4821</div>
    <div class="contact-item">rtvengineering-hq.example</div>
    <div class="contact-item">4180 Harbor Point Road, Suite<br>310 Bayview, VA 20000</div>
  </div>

  <ul class="services">
    <li class="service"><div class="service__icon"><span></span></div><div class="service__text">ACQUISITION &amp; PROGRAM<br>MANAGEMENT</div></li>
    <li class="service"><div class="service__icon"><span></span></div><div class="service__text">INTELLIGENCE &amp; SECURITY<br>OPERATIONS</div></li>
    <li class="service"><div class="service__icon"><span></span></div><div class="service__text">CYBER, IT &amp; NETWORK<br>OPERATIONS</div></li>
    <li class="service"><div class="service__icon"><span></span></div><div class="service__text">LIFECYCLE LOGISTICS &amp;<br>ASSET READINESS</div></li>
    <li class="service"><div class="service__icon"><span></span></div><div class="service__text">C5ISR SYSTEMS ENGINEERING<br>&amp; SUSTAINMENT</div></li>
  </ul>

  <div class="brand-name back__name">RTV ENGINEERING</div>
</section>

</body>
</html>
```